BOLD & MINIMALIST DESIGN NEEDED

We want a very bold but minimalistic business card design that is impactful and utilizes both sides of the business card. Our current logo is included for your use.

We want bold fonts and good use of negative space. We don't want the logo to overpower the design.

Target Market(s)

Professionals who are building new commercial buildings.

Industry/Entity Type

Construction

Contact Information for Business Card

Name, Title, email, office phone, cell phone, website

Font styles to use
Serif
Sans Serif

Requirements
Must have
• Bold design!

```html
<!DOCTYPE html>
<html lang="en">
<head>
<meta charset="utf-8">
<title>Stonecrest Build — Business Card</title>
<link href="https://fonts.googleapis.com/css2?family=Poppins:wght@400;500;700&display=swap" rel="stylesheet">
<style>
  :root {
    --backdrop: #262626;
    --card-top: #232323;
    --card-bottom: #1a1a1a;
    --ink-light: #e8e8e8;
    --ink-soft: #d4d4d4;
    --accent: #7dc242;
  }
  * { box-sizing: border-box; margin: 0; padding: 0; }
  html, body {
    width: 1200px; height: 576px; overflow: hidden;
    background: var(--backdrop);
    font-family: "Poppins", sans-serif;
  }
  .canvas { position: relative; width: 1200px; height: 576px; }
  .card {
    position: absolute; top: 139px; height: 293px;
    border-radius: 10px;
    background: linear-gradient(180deg, var(--card-top), var(--card-bottom));
  }
  .card--front { left: 102px; width: 484px; }
  .card--back  { left: 597px; width: 479px; }

  .wordmark {
    display: flex; align-items: center; gap: 10px;
    color: var(--ink-light); font-weight: 700;
    text-transform: uppercase; letter-spacing: 0.06em; white-space: nowrap;
  }
  .wordmark__mark { background: var(--accent); flex: none; }

  .card--front .wordmark {
    position: absolute; left: 50%; top: 50%;
    transform: translate(-50%, -50%);
    font-size: 30px;
  }
  .card--front .wordmark__mark { width: 22px; height: 22px; }

  .card--back .wordmark {
    position: absolute; left: 30px; bottom: 38px;
    font-size: 17px; gap: 7px;
  }
  .card--back .wordmark__mark { width: 13px; height: 13px; }

  .identity {
    position: absolute; right: 30px; top: 30px; text-align: right;
  }
  .identity__name {
    color: var(--accent); font-size: 21px; font-weight: 500; line-height: 1.2;
  }
  .identity__title {
    color: var(--ink-soft); font-size: 12px; line-height: 1.4;
  }

  .contact {
    position: absolute; right: 30px; bottom: 34px;
    list-style: none; text-align: right;
  }
  .contact__item {
    display: flex; justify-content: flex-end; align-items: center; gap: 7px;
    color: var(--ink-soft); font-size: 12px; line-height: 16.5px;
  }
  .contact__icon { width: 10px; height: 10px; fill: var(--accent); flex: none; }
</style>
</head>
<body>
<main class="canvas">
  <section class="card card--front">
    <div class="wordmark"><span class="wordmark__mark"></span>Stonecrest Build</div>
  </section>

  <section class="card card--back">
    <header class="identity">
      <p class="identity__name">Daniel Reyes</p>
      <p class="identity__title">Director</p>
    </header>

    <div class="wordmark"><span class="wordmark__mark"></span>Stonecrest Build</div>

    <ul class="contact">
      <li class="contact__item">555-014-2200
        <svg class="contact__icon" viewBox="0 0 10 10" aria-hidden="true"><path d="M1 3.5C1 2 2.5 1 5 1s4 1 4 2.5L7.5 4.2 6.6 3H3.4L2.5 4.2zM2.5 5h5L8.5 9h-7z"/></svg>
      </li>
      <li class="contact__item">daniel@stonecrestbuild.com
        <svg class="contact__icon" viewBox="0 0 10 10" aria-hidden="true"><path d="M0 2h10v6H0zM.8 2.6 5 5.8l4.2-3.2"/><path d="M.8 2.6 5 5.8l4.2-3.2" fill="none" stroke="#1e1e1e" stroke-width=".9"/></svg>
      </li>
      <li class="contact__item">www.stonecrestbuild.com
        <svg class="contact__icon" viewBox="0 0 10 10" aria-hidden="true"><circle cx="5" cy="5" r="4.5"/><path d="M.5 5h9M5 .5v9M5 .5C3 3 3 7 5 9.5M5 .5C7 3 7 7 5 9.5" fill="none" stroke="#1e1e1e" stroke-width=".7"/></svg>
      </li>
    </ul>
  </section>
</main>
</body>
</html>
```